BRIXLEY ELECTRICAL

all black background with silver and lime writing, fonts i like are gothic style but am open to ideas, will need a picture logo aswell as im putting this on my van.i am a electrical contractor starting up my own electrical business. underneath brixley electrical heading on card we could put" professiona cost effective soloutions to all your electrical needs".{ or something of that nature }.on aback of card on top half list servises provided, real estate and commercial maintenance, new home and renovation rewires and upgrades, split system air conditioning, floor heat, tv phone data, smoke detoctors, lighting systems , builders welcome, , and also a thankyou for your business.

Industry/Entity Type

Real Estate

Contact Information for Business Card

GAVIN PRESTWORTH
brixleyelectrical@quillnet.com.au
0417352940
lic no 81926
ac lic no l593721
abn 37216405813

```html
<!DOCTYPE html>
<html lang="en">
<head>
<meta charset="utf-8">
<title>Brixley Electrical – Business Card</title>
<link rel="stylesheet" href="https://fonts.googleapis.com/css2?family=Questrial&display=swap">
<style>
  :root {
    --stage: #c8c8c8;
    --card-black: #050505;
    --lime: #8cc63f;
    --lime-bright: #9bd133;
    --silver: #8a8a8a;
    --band-line: #5b5b5b;
    --ink-dark: #141414;
  }
  * { box-sizing: border-box; margin: 0; padding: 0; }
  html, body {
    width: 1200px;
    height: 1000px;
    overflow: hidden;
  }
  body {
    position: relative;
    background: var(--stage);
    font-family: "Questrial", "Century Gothic", sans-serif;
  }
  .card {
    position: absolute;
    width: 700px;
    height: 428px;
    background: var(--card-black);
    overflow: hidden;
    box-shadow: 0 6px 18px rgba(0,0,0,0.25);
  }
  .card--back { left: 420px; top: 50px; }
  .card--front { left: 80px; top: 510px; }

  /* Services list */
  .services {
    position: absolute;
    left: 62px;
    top: 42px;
    list-style: none;
    color: var(--lime-bright);
    font-size: 19px;
    line-height: 23px;
  }

  /* Brand lockup */
  .brand {
    position: absolute;
    display: flex;
    flex-direction: column;
    align-items: center;
  }
  .brand__dot {
    width: 74px;
    height: 74px;
    border-radius: 50%;
    background: var(--lime);
    margin-bottom: 8px;
  }
  .brand__name {
    color: var(--lime);
    font-size: 27px;
    letter-spacing: 1.5px;
    white-space: nowrap;
  }
  .brand__tagline {
    color: var(--silver);
    font-size: 10.5px;
    margin-top: 2px;
    white-space: nowrap;
  }
  .card--back .brand { right: 34px; bottom: 48px; }
  .card--front .brand { left: 338px; top: 70px; }

  /* Contact block */
  .contact {
    position: absolute;
    left: 70px;
    top: 86px;
    color: var(--lime);
  }
  .contact__name { font-size: 24px; letter-spacing: 0.5px; }
  .contact__phone { font-size: 20px; margin-bottom: 22px; }
  .contact__line { font-size: 20px; line-height: 25px; }

  /* Email band */
  .band-rule {
    position: absolute;
    left: 0; right: 0;
    top: 300px;
    height: 10px;
    background: var(--band-line);
  }
  .band {
    position: absolute;
    left: 0; right: 0;
    top: 310px;
    bottom: 0;
    background: var(--lime);
    display: flex;
    align-items: center;
    justify-content: center;
  }
  .band__email {
    color: var(--ink-dark);
    font-size: 25px;
    letter-spacing: 0.3px;
  }

  /* Small lockup swatch */
  .swatch {
    position: absolute;
    left: 908px;
    top: 782px;
    width: 270px;
    height: 160px;
    background: var(--card-black);
  }
  .swatch .brand { left: 0; right: 0; top: 22px; }
  .swatch .brand__dot { width: 52px; height: 52px; margin-bottom: 6px; }
  .swatch .brand__name { font-size: 19px; letter-spacing: 1px; }
  .swatch .brand__tagline { font-size: 7.5px; }
</style>
</head>
<body>

  <section class="card card--back" aria-label="Business card back">
    <ul class="services">
      <li>Real Estate and Commercial Maintenance</li>
      <li>New Home and Renovation Rewires and Upgrades</li>
      <li>Split System Air Conditioning</li>
      <li>Floor Feat</li>
      <li>TV Phone Data</li>
      <li>Smoke Detectors</li>
      <li>Lighting Systems</li>
      <li>Builders Welcome</li>
    </ul>
    <div class="brand">
      <span class="brand__dot"></span>
      <span class="brand__name">BRIXLEY ELECTRICAL</span>
      <span class="brand__tagline">Professional cost effective soloutions to all your electrical needs</span>
    </div>
  </section>

  <section class="card card--front" aria-label="Business card front">
    <div class="contact">
      <p class="contact__name">GAVIN PRESTWORTH</p>
      <p class="contact__phone">+ 0417352940</p>
      <p class="contact__line">LIC No : 81926</p>
      <p class="contact__line">AC LIC No : l593721</p>
      <p class="contact__line">ABN : 37216405813</p>
    </div>
    <div class="brand">
      <span class="brand__dot"></span>
      <span class="brand__name">BRIXLEY ELECTRICAL</span>
      <span class="brand__tagline">Professional cost effective soloutions to all your electrical needs</span>
    </div>
    <div class="band-rule"></div>
    <div class="band">
      <span class="band__email">brixleyelectrical@quillnet.com.au</span>
    </div>
  </section>

  <section class="swatch" aria-label="Brand lockup">
    <div class="brand">
      <span class="brand__dot"></span>
      <span class="brand__name">BRIXLEY ELECTRICAL</span>
      <span class="brand__tagline">Professional cost effective soloutions to all your electrical needs</span>
    </div>
  </section>

</body>
</html>
```